Fire Protection Company

Hi we have a company called Brenlow Protection Services and are looking for a new design we are wanting flames as the last card was great with the whole background flames but you cant really see the services offered, phone, names etc.

We need something more upmarket and professional and only have a small budget

We need the words Brenlow Protection Services, Marcus Pelwey MSBuildA - Fire Safety Consultant, Phone No 0427316508 address : PO Box 8163 TRDC 4852 ABN 71264085319, HVRA Lic.5382410 Email marcus@brenlowgroup.example.com.au

Industry/Entity Type

Fire Safety

Font styles to use
Sans Serif

Colors
ec2027
ffc214

```html
<!DOCTYPE html>
<html lang="en">
<head>
<meta charset="utf-8">
<title>Brenlow Protection Services – Business Card &amp; Wordmark</title>
<link rel="stylesheet" href="https://fonts.googleapis.com/css2?family=Roboto:wght@400;500;700;900&display=swap">
<style>
  :root {
    --brand-red: #ec2027;
    --brand-yellow: #ffc214;
    --ink: #231f20;
    --text-grey: #3a3a3a;
    --paper: #ffffff;
    --board: #ffffff;
    --black: #000000;
  }
  * { box-sizing: border-box; margin: 0; padding: 0; }
  html, body {
    width: 1200px; height: 848px; overflow: hidden;
    background: var(--board);
    font-family: "Roboto", Arial, sans-serif;
  }
  .board { position: relative; width: 1200px; height: 848px; }

  .card {
    position: absolute; top: 249px; width: 343px; height: 222px;
    box-shadow: 0 6px 10px rgba(0,0,0,0.22);
    overflow: hidden;
  }
  .card--front { left: 239px; background: var(--brand-red); }
  .card--back { left: 623px; background: var(--paper); }

  .wordmark {
    display: flex; align-items: center; gap: 6px;
    font-weight: 900; letter-spacing: -1px; line-height: 1;
    white-space: nowrap;
  }
  .wordmark__dot { border-radius: 50%; flex: none; }

  .card--front .wordmark {
    position: absolute; left: 0; right: 0; top: 66px;
    justify-content: center; color: var(--paper); font-size: 46px;
  }
  .card--front .wordmark__dot { width: 38px; height: 38px; background: var(--paper); }
  .tagline {
    position: absolute; left: 0; right: 0; top: 134px;
    text-align: center; color: var(--paper);
    font-weight: 700; font-size: 18.5px; letter-spacing: -0.3px;
  }
  .tagline__bullet {
    display: inline-block; width: 6px; height: 6px; border-radius: 50%;
    background: var(--paper); vertical-align: middle; margin: 0 6px 3px;
  }

  .contact-block { position: absolute; left: 28px; top: 28px; }
  .contact-block__company { color: var(--brand-red); font-weight: 700; font-size: 12.5px; }
  .contact-block__name { color: var(--ink); font-weight: 500; font-size: 12.5px; margin-top: 2px; letter-spacing: 0.2px; }
  .contact-block__role { color: var(--ink); font-size: 12.5px; margin-top: 3px; }
  .contact-block__rule { width: 207px; height: 2px; background: var(--brand-red); margin-top: 7px; }

  .contact-list { position: absolute; left: 28px; top: 100px; list-style: none; }
  .contact-list li {
    display: flex; align-items: flex-start; gap: 8px;
    color: var(--text-grey); font-size: 11.5px; line-height: 15.5px;
    margin-bottom: 9px;
  }
  .contact-list svg { width: 13px; height: 13px; flex: none; margin-top: 1px; fill: var(--brand-red); }
  .contact-list__email { font-size: 10.5px; }

  .card__ring { position: absolute; left: 256px; top: 36px; width: 150px; height: 150px; }

  .logo-variant {
    position: absolute; top: 714px; width: 306px; height: 72px;
    display: flex; align-items: center;
  }
  .logo-variant .wordmark { font-size: 58px; letter-spacing: -2px; }
  .logo-variant .wordmark__dot { width: 50px; height: 50px; }
  .logo-variant--colour { left: 68px; }
  .logo-variant--colour .wordmark { color: var(--brand-red); }
  .logo-variant--colour .wordmark__dot { background: var(--brand-red); }
  .logo-variant--mono { left: 414px; }
  .logo-variant--mono .wordmark { color: var(--black); }
  .logo-variant--mono .wordmark__dot { background: var(--black); }
  .logo-variant--reverse {
    left: 766px; top: 688px; width: 365px; height: 138px; background: var(--black);
    justify-content: center;
  }
  .logo-variant--reverse .wordmark { color: var(--paper); }
  .logo-variant--reverse .wordmark__dot { background: var(--paper); }
</style>
</head>
<body>
<main class="board">

  <section class="card card--front" aria-label="Business card front">
    <div class="wordmark"><span class="wordmark__dot"></span>BRENLOW</div>
    <p class="tagline"><span class="tagline__bullet"></span>PROTECTION SERVICES<span class="tagline__bullet"></span></p>
  </section>

  <section class="card card--back" aria-label="Business card back">
    <div class="contact-block">
      <p class="contact-block__company">BRENLOW PROTECTION SERVICES</p>
      <p class="contact-block__name">MARCUS PELWEY MSBUILDA</p>
      <p class="contact-block__role">Fire Safety Consultant</p>
      <div class="contact-block__rule"></div>
    </div>
    <ul class="contact-list">
      <li>
        <svg viewBox="0 0 16 16" aria-hidden="true"><path d="M1 5c0-2 3-3 7-3s7 1 7 3v1.5h-3.5V5H4.5v1.5H1z"/><path d="M3 8l2-2h6l2 2v5H3z"/><circle cx="8" cy="10" r="1.6" fill="#fff"/></svg>
        <span>0427316508</span>
      </li>
      <li>
        <svg viewBox="0 0 16 16" aria-hidden="true"><path d="M8 1a5 5 0 0 0-5 5c0 3.5 5 9 5 9s5-5.5 5-9a5 5 0 0 0-5-5zm0 7a2 2 0 1 1 0-4 2 2 0 0 1 0 4z"/></svg>
        <span>PO Box 8163 TRDC 4852<br>ABN 71264085319<br>HVRA Lic.5382410</span>
      </li>
      <li>
        <svg viewBox="0 0 16 16" aria-hidden="true"><path d="M1 3h14v10H1z"/><path d="M2 4l6 5 6-5" fill="none" stroke="#fff" stroke-width="1.4"/></svg>
        <span class="contact-list__email">marcus@brenlowgroup.example.com.au</span>
      </li>
    </ul>
    <svg class="card__ring" viewBox="0 0 150 150" aria-hidden="true">
      <circle cx="75" cy="75" r="62" fill="none" stroke="var(--brand-red)" stroke-width="22"/>
    </svg>
  </section>

  <div class="logo-variant logo-variant--colour">
    <div class="wordmark"><span class="wordmark__dot"></span>BRENLOW</div>
  </div>
  <div class="logo-variant logo-variant--mono">
    <div class="wordmark"><span class="wordmark__dot"></span>BRENLOW</div>
  </div>
  <div class="logo-variant logo-variant--reverse">
    <div class="wordmark"><span class="wordmark__dot"></span>BRENLOW</div>
  </div>

</main>
</body>
</html>
```